TALMERA Stationary and Biz Card design
TALMERA Economic Development Company
TALMERA Stationary and Biz Card design - Financial Services
Creative Brief
Professional
Dennis P Wexford
CEO
PO BOX 782 FAIRHOLT, MAINE 04987
dennis@talmeraco.example
talmeraco.example
Looking for designs that encompass the strength and integrity of the logo.

```html
<!DOCTYPE html>
<html lang="en">
<head>
<meta charset="utf-8">
<title>TALMERA Stationery and Business Card</title>
<link rel="stylesheet" href="https://fonts.googleapis.com/css2?family=Montserrat:wght@400;600;700&display=swap">
<style>
  :root {
    --stage: #3b3b3d;
    --paper: #ffffff;
    --paper-shade: #f1f2f4;
    --navy: #1f3a6b;
    --grey-env: #6e6f72;
    --ink: #3a3d44;
    --muted: #8a8d94;
    --label: #c9c9cc;
    --mark-soft: #e6e8ec;
  }
  * { box-sizing: border-box; margin: 0; padding: 0; }
  html, body { width: 1200px; height: 430px; overflow: hidden; }
  body {
    background: var(--stage);
    font-family: "Montserrat", Arial, sans-serif;
    color: var(--ink);
    position: relative;
  }
  .item {
    position: absolute;
    background: var(--paper);
    box-shadow: 0 3px 8px rgba(0,0,0,.45);
    overflow: hidden;
  }
  .caption {
    position: absolute;
    font-size: 7px;
    color: var(--label);
    text-align: center;
  }
  .brand {
    font-weight: 700;
    letter-spacing: .22em;
    color: var(--navy);
    display: flex;
    align-items: center;
    gap: .4em;
    white-space: nowrap;
  }
  .brand .dot {
    width: .8em; height: .8em; border-radius: 50%;
    background: var(--navy);
  }
  .brand.on-dark { color: var(--paper); }
  .brand.on-dark .dot { background: var(--paper); }
  .faint-mark {
    position: absolute;
    border-radius: 45% 55% 40% 50%;
    background: radial-gradient(ellipse at 40% 40%, var(--mark-soft), rgba(230,232,236,0) 70%);
  }
  .small { font-size: 5px; line-height: 1.5; color: var(--muted); }

  /* business card front */
  .card-front { left: 24px; top: 24px; width: 192px; height: 96px; }
  .card-front .brand { position: absolute; left: 10px; top: 10px; font-size: 9px; }
  .card-front .person { position: absolute; left: 10px; top: 28px; }
  .card-front .name { font-size: 6px; font-weight: 600; color: var(--navy); }
  .card-front .faint-mark { right: -10px; top: 14px; width: 120px; height: 80px; }

  /* business card back, white */
  .card-back { left: 24px; top: 168px; width: 192px; height: 96px; }
  .card-back .faint-mark { left: -6px; top: 6px; width: 120px; height: 90px; }
  .card-back .brand { position: absolute; right: 12px; top: 40px; font-size: 10px; }
  .card-back .tag { position: absolute; right: 12px; top: 54px; font-size: 4px; color: var(--muted); letter-spacing: .1em; }

  /* business card back, navy */
  .card-navy { left: 24px; top: 298px; width: 192px; height: 96px; background: var(--navy); }
  .card-navy .brand { position: absolute; left: 14px; top: 58px; font-size: 10px; }

  /* letterheads */
  .letterhead { top: 24px; width: 271px; height: 374px; }
  .letterhead.one { left: 233px; }
  .letterhead.two { left: 523px; }
  .letterhead .brand { position: absolute; left: 20px; top: 28px; font-size: 12px; }
  .letterhead .contact { position: absolute; right: 20px; top: 16px; }
  .letterhead .faint-mark { left: 20px; top: 200px; width: 230px; height: 170px; }
  .letterhead .footer { position: absolute; left: 0; right: 0; bottom: 12px; text-align: center; font-size: 4px; color: var(--muted); }
  .letterhead.two .brand { top: 20px; }

  /* envelopes */
  .envelope { left: 811px; width: 377px; }
  .env-grey { top: 24px; height: 84px; background: var(--grey-env); }
  .env-grey .brand { position: absolute; left: 152px; top: 34px; font-size: 11px; }
  .env-navy { top: 86px; height: 106px; background: var(--navy); }
  .env-navy .brand { position: absolute; left: 150px; top: 44px; font-size: 11px; }
  .env-plain { top: 192px; height: 96px; background: var(--paper-shade); }
  .env-front { top: 252px; height: 132px; }
  .env-front .brand { position: absolute; left: 14px; top: 12px; font-size: 11px; }
  .env-front .return { position: absolute; left: 14px; top: 30px; }
  .env-front .faint-mark { right: 20px; top: 20px; width: 170px; height: 110px; }
  .flap { position: absolute; inset: 0; width: 100%; height: 100%; }
</style>
</head>
<body>

  <section class="item card-front">
    <div class="brand"><span class="dot"></span>TALMERA</div>
    <div class="person">
      <p class="name">Dennis P Wexford</p>
      <p class="small">CEO<br>PO BOX 782 FAIRHOLT, MAINE 04987<br>207-555-0148<br>dennis@talmeraco.example</p>
    </div>
    <div class="faint-mark" role="img" aria-label="Faint lion emblem decoration"></div>
  </section>
  <p class="caption" style="left:24px;top:126px;width:192px;">Business Card</p>

  <section class="item card-back">
    <div class="faint-mark" role="img" aria-label="Faint lion emblem decoration"></div>
    <div class="brand">TALMERA</div>
    <p class="tag">ECONOMIC DEVELOPMENT</p>
  </section>
  <p class="caption" style="left:24px;top:270px;width:192px;">Back Card Option #1</p>

  <section class="item card-navy">
    <div class="brand on-dark"><span class="dot"></span>TALMERA</div>
  </section>
  <p class="caption" style="left:24px;top:400px;width:192px;">Back Card Option #2</p>

  <section class="item letterhead one">
    <div class="brand"><span class="dot"></span>TALMERA</div>
    <p class="contact small">207-555-0148<br>207-555-0172<br>dennis@talmeraco.example<br>talmeraco.example</p>
    <div class="faint-mark" role="img" aria-label="Large faint lion emblem watermark"></div>
    <p class="footer">talmeraco.example</p>
  </section>
  <p class="caption" style="left:233px;top:406px;width:271px;">Letterhead Option #1</p>

  <section class="item letterhead two">
    <div class="brand"><span class="dot"></span>TALMERA</div>
    <div class="faint-mark" role="img" aria-label="Large faint lion emblem watermark"></div>
    <p class="footer">PO BOX 782 FAIRHOLT, MAINE 04987 · 207-555-0148 · dennis@talmeraco.example · talmeraco.example</p>
  </section>
  <p class="caption" style="left:523px;top:406px;width:271px;">Letterhead Option #2</p>

  <section class="item envelope env-grey">
    <svg class="flap" viewBox="0 0 377 84" preserveAspectRatio="none"><path d="M0 0 L188 50 L377 0" fill="none" stroke="#5d5e61" stroke-width="1"/></svg>
    <div class="brand on-dark"><span class="dot"></span>TALMERA</div>
  </section>
  <section class="item envelope env-navy">
    <svg class="flap" viewBox="0 0 377 106" preserveAspectRatio="none"><path d="M0 0 L188 70 L377 0" fill="none" stroke="#18305a" stroke-width="1"/></svg>
    <div class="brand on-dark"><span class="dot"></span>TALMERA</div>
  </section>
  <section class="item envelope env-plain">
    <svg class="flap" viewBox="0 0 377 96" preserveAspectRatio="none"><path d="M0 0 L188 56 L377 0" fill="none" stroke="#d8dadf" stroke-width="1"/></svg>
  </section>
  <section class="item envelope env-front">
    <div class="brand"><span class="dot"></span>TALMERA</div>
    <p class="return small">PO BOX 782 FAIRHOLT, MAINE 04987</p>
    <div class="faint-mark" role="img" aria-label="Faint lion emblem decoration"></div>
  </section>
  <p class="caption" style="left:811px;top:392px;width:377px;">Envelope Options #1</p>

</body>
</html>
```